Tolvex Engineers: Why you should hire us keepsake

New design. Open to plastic cards. We are an engineering firm that designs cell phone towers and commercial buildings. Please check out our website www.tolvexgrp.com for more details. We want people to remember our card and for it to be useful if possible. We want the same look and feel on these cards to be translated to other marketing material we may need such as brochures.

Target Market(s)

Architects, Developers and Telecommunication Carriers

Industry/Entity Type

Engineering

Contact Information for Business Card

Card with our company colors, logo, and innovative design with elements related to our industry.

Font styles to use
Sans Serif

Colors
9bcb3c
abd036
0255a3

Requirements
Must have
• Sleek and hip design
Nice to have
• Bright lime green and navy coloring that pops with an innovative design.
Should not have
• A basic and boring design

```html
<!DOCTYPE html>
<html lang="en">
<head>
<meta charset="utf-8">
<title>Tolvex Engineers – Business Card</title>
<link rel="stylesheet" href="https://fonts.googleapis.com/css2?family=Roboto:wght@400;500&family=Roboto+Condensed:wght@700&display=swap">
<style>
  :root {
    --backdrop: #2a2a2a;
    --paper: #f2f2f2;
    --lime: #00f000;
    --navy: #0d2a6e;
    --ink: #4a4a4a;
    --rule: #b8b8b8;
    --white: #ffffff;
  }
  * { margin: 0; padding: 0; box-sizing: border-box; }
  html, body { width: 1200px; height: 960px; overflow: hidden; }
  body {
    position: relative;
    background: var(--backdrop);
    font-family: "Roboto", Arial, sans-serif;
  }
  .card {
    position: absolute;
    width: 600px;
    height: 343px;
  }
  .card--front { left: 314px; top: 113px; background: var(--paper); }
  .card--back { left: 311px; top: 472px; background: var(--lime); }

  .wordmark {
    position: absolute;
    font-family: "Roboto Condensed", Arial, sans-serif;
    font-weight: 700;
    letter-spacing: -1px;
    line-height: 1;
  }
  .card--front .wordmark {
    left: 54px; top: 134px;
    font-size: 74px;
    color: var(--lime);
  }
  .card--back .wordmark {
    left: 0; right: 0; top: 112px;
    text-align: center;
    font-size: 98px;
    color: var(--navy);
  }

  .divider {
    position: absolute;
    left: 304px; top: 109px;
    width: 1px; height: 128px;
    background: var(--rule);
  }
  .contact { position: absolute; left: 332px; top: 116px; }
  .contact__name {
    font-family: "Roboto Condensed", Arial, sans-serif;
    font-weight: 700;
    font-size: 21px;
    color: var(--lime);
    margin-bottom: 9px;
  }
  .contact__list { list-style: none; }
  .contact__item {
    display: flex;
    align-items: center;
    gap: 9px;
    height: 19px;
    font-size: 14.5px;
    color: var(--ink);
  }
  .contact__icon { width: 13px; height: 13px; fill: var(--lime); flex: none; }

  .tagline {
    position: absolute;
    left: 0; right: 0; top: 265px;
    display: flex;
    justify-content: center;
    align-items: center;
    gap: 4px;
    color: var(--white);
    font-weight: 500;
    font-size: 16.5px;
  }
  .tagline__rule { width: 30px; height: 1px; background: var(--white); }
  .locations {
    position: absolute;
    left: 0; right: 0; top: 288px;
    text-align: center;
    color: var(--white);
    font-size: 15px;
    letter-spacing: 0.8px;
  }
</style>
</head>
<body>
  <section class="card card--front" aria-label="Business card front">
    <div class="wordmark">TOLVEX</div>
    <div class="divider"></div>
    <div class="contact">
      <div class="contact__name">DANA REYES HOLT</div>
      <ul class="contact__list">
        <li class="contact__item">
          <svg class="contact__icon" viewBox="0 0 16 16" aria-hidden="true"><path d="M3 1l3 3-1.5 2c1 2 3.5 4.5 5.5 5.5L12 10l3 3-2 2C7 15 1 9 1 3z"/></svg>
          555.013.4170
        </li>
        <li class="contact__item">
          <svg class="contact__icon" viewBox="0 0 16 16" aria-hidden="true"><path d="M4 0h8v16H4zM5.5 2v10h5V2zM7 13.5h2v1H7z" fill-rule="evenodd"/></svg>
          555.018.6294
        </li>
        <li class="contact__item">
          <svg class="contact__icon" viewBox="0 0 16 16" aria-hidden="true"><path d="M1 4h14v9H1z"/><path d="M1.5 4.5L8 9l6.5-4.5" stroke="#f2f2f2" stroke-width="1.2" fill="none"/></svg>
          dholt@tolvexgrp.com
        </li>
        <li class="contact__item">
          <svg class="contact__icon" viewBox="0 0 16 16" aria-hidden="true"><circle cx="8" cy="8" r="7"/><path d="M4 5c2 0 2 2 4 2s1 3 0 4M10 3c0 2 2 2 3 3" stroke="#f2f2f2" stroke-width="1.4" fill="none"/></svg>
          www.tolvexgrp.com
        </li>
      </ul>
    </div>
  </section>

  <section class="card card--back" aria-label="Business card back">
    <div class="wordmark">TOLVEX</div>
    <div class="tagline"><span class="tagline__rule"></span>MULTI-DISCIPLINE ENGINEERING<span class="tagline__rule"></span></div>
    <div class="locations">Denver | Raleigh | Tulsa | Sacramento</div>
  </section>
</body>
</html>
```